Poster Design Project

Need a design for a music festival called Counter-Lanternweek

The design needs to have areas for the following:
- Band Names
- DJ Names
- Sponsor Names and Logos
- Event location, Date & Time

Industry/Entity Type

Festival

```html
<!DOCTYPE html>
<html lang="en">
<head>
<meta charset="utf-8">
<title>Counter-Lanternweek Festival Poster</title>
<link rel="stylesheet" href="https://fonts.googleapis.com/css2?family=Rubik+Distressed&family=Great+Vibes&family=Alfa+Slab+One&family=Open+Sans:ital,wght@0,700;1,800&family=Patrick+Hand&display=swap">
<style>
  :root {
    --bg-black: #050505;
    --glow-green: #1fa21a;
    --glow-white: #ffffff;
    --beam-green: #8dfc8a;
    --beam-yellow: #d9d32a;
    --sponsor-red: #c8200c;
    --title-red: #b8202a;
    --title-outline: #f1e9e4;
    --slab-fill: #e4e4e4;
    --slab-shadow: #8a1e1e;
    --event-red: #d23a14;
    --square-blue: #2f5ff5;
    --square-orange: #f08a2a;
    --strip-red: #9b1010;
    --ink: #0a0a0a;
  }
  * { margin: 0; padding: 0; box-sizing: border-box; }
  html, body {
    width: 849px; height: 1200px; overflow: hidden; background: var(--bg-black);
  }
  .poster {
    position: relative; width: 849px; height: 1200px; overflow: hidden;
    background:
      radial-gradient(circle at 385px 60px, rgba(31,162,26,.9) 0, rgba(31,162,26,0) 70px),
      radial-gradient(circle at 770px 95px, rgba(31,162,26,.95) 0, rgba(31,162,26,.5) 90px, rgba(31,162,26,0) 200px),
      radial-gradient(circle at 60px 260px, rgba(31,162,26,.55) 0, rgba(31,162,26,0) 200px),
      radial-gradient(ellipse 280px 260px at 640px 390px, #ffffff 0, rgba(255,255,255,.85) 40%, rgba(255,255,255,0) 100%),
      radial-gradient(ellipse 700px 900px at 420px 560px, #6a6a6a 0, #2a2a2a 50%, var(--bg-black) 100%);
  }
  .decor { position: absolute; inset: 0; }
  .performer-art {
    position: absolute; left: 68px; top: 190px; width: 700px; height: 860px;
    clip-path: polygon(30% 0, 62% 0, 66% 30%, 100% 50%, 100% 72%, 72% 100%, 0 100%, 0 26%);
    background: linear-gradient(160deg, #6d5a8e 0%, #a8573f 20%, #1c1c1c 45%, #3a2a22 70%, #c77a3a 100%);
    opacity: .85;
  }
  .sponsor-label {
    position: absolute; left: 104px; top: 104px; width: 150px; text-align: center;
    font: italic 800 27px "Open Sans", sans-serif; color: #fff;
  }
  .band-name {
    position: absolute; left: 570px; top: 330px; width: 240px; text-align: center;
    font: 64px/1.15 "Rubik Distressed", sans-serif; color: var(--ink);
  }
  .dj-names {
    position: absolute; left: 600px; top: 494px; width: 200px; text-align: center;
    font: 36px "Patrick Hand", sans-serif; color: var(--ink);
  }
  .festival-title { position: absolute; left: 0; top: 0; }
  .title-script {
    position: absolute; left: 28px; top: 770px; white-space: nowrap;
    font: 200px/1 "Great Vibes", cursive; color: var(--title-red);
    -webkit-text-stroke: 5px var(--title-outline); paint-order: stroke fill;
  }
  .title-slab {
    position: absolute; left: 212px; top: 1052px; width: 600px; text-align: right; white-space: nowrap;
    font: 62px/1 "Alfa Slab One", serif; letter-spacing: 0; color: var(--slab-fill);
    -webkit-text-stroke: 1.5px #333;
    text-shadow: 4px 4px 0 var(--slab-shadow), 6px 6px 0 #111;
    transform: scaleX(.86); transform-origin: right center;
  }
  .event-details {
    position: absolute; left: 180px; top: 1140px; width: 632px; text-align: right;
    font: 700 33px "Open Sans", sans-serif; color: var(--event-red);
  }
</style>
</head>
<body>
<main class="poster">
  <svg class="decor" width="849" height="1200" viewBox="0 0 849 1200" aria-hidden="true">
    <polygon class="light-beam" points="400,500 735,215 830,275" fill="var(--beam-green)" opacity=".85"/>
    <polygon class="light-beam" points="410,515 760,470 765,500" fill="var(--beam-green)" opacity=".6"/>
    <polygon class="light-beam" points="330,420 840,900 840,960 300,470" fill="var(--beam-yellow)" opacity=".8"/>
    <rect class="edge-strip" x="820" y="407" width="29" height="612" fill="var(--strip-red)"/>
    <rect class="square" x="102" y="234" width="82" height="82" fill="var(--square-blue)"/>
    <rect class="square" x="535" y="190" width="68" height="68" fill="#fff"/>
    <rect class="square" x="518" y="543" width="26" height="22" fill="var(--square-orange)"/>
    <rect class="square" x="583" y="533" width="12" height="12" fill="var(--square-blue)"/>
    <rect class="square" x="730" y="540" width="30" height="24" fill="var(--beam-green)" opacity=".7"/>
    <rect class="square" x="730" y="858" width="34" height="32" fill="#3a1466"/>
    <rect class="square" x="108" y="858" width="30" height="28" fill="#1d5a1d"/>
    <polygon class="sponsor-burst" fill="var(--sponsor-red)"
      points="314,127 257,141 296,174 236,166 246,208 199,181 178,220 157,181 110,208 120,166 60,174 99,141 42,127 99,113 60,80 120,88 110,46 157,73 178,34 199,73 246,46 236,88 296,80 257,113"/>
  </svg>

  <div class="performer-art" role="img" aria-label="Illustration of a bass guitarist in a bandana performing under stage lights"></div>

  <div class="sponsor-label">Sponsor</div>

  <h2 class="band-name">NAME<br>BAND</h2>
  <p class="dj-names">DJ Names</p>

  <h1 class="festival-title">
    <span class="title-script">Counter-</span>
    <span class="title-slab">LANTERNWEEK</span>
  </h1>

  <p class="event-details">Event location, Date &amp; Time</p>
</main>
</body>
</html>
```